Skyforge Technics Inc. - new Website

1 - Take the existing content and elevate the site to be much more dynamic. www.skyforgenorth.example. We are looking for a site that is modern and easily updated. Aerospace is our primary industry but rail and engineering are part of who we are.

2- New logo to implement (attached)

3 - Remove customer access page

4 - website to be built so that we can change and update from our offices with no coding requirements.

5 - Pictures available

6 - Bilingual French and English

7 - News / Press page

8 - Social media icons link Twitter, youtube and linkedin

9 - add an PLUME engineering page (content will be added later) Plume logo attached

10 - Please use stock photos, and but will pay for royalty if necessary

Target Market(s)

Airlines 80%
Rail 10%
Other transportation 10%

Industry/Entity Type

Aviation

Number of Pages Required

5+ page

Font styles to use
Sans Serif

Requirements
Must have
• Skyforge logo
• Logo Plume (Skyforge Validation Bureau Partners inc.)
• Dynamic modern look and feel
• Existing content from our website and attched introduction document plus the above
• Press page
• Industry pictures - Repair (as per our website)
Nice to have
• Animation
• You tube links
• Blog
• Career page

```html
<!DOCTYPE html>
<html lang="en">
<head>
<meta charset="utf-8">
<title>Skyforge Technics Inc.</title>
<link rel="stylesheet" href="https://fonts.googleapis.com/css2?family=Open+Sans:wght@400;600;700&display=swap">
<style>
:root{
  --blue:#1f6fb8;
  --navy:#183f73;
  --footer:#2a6db4;
  --footer-dark:#1d528d;
  --red:#d7332b;
  --ink:#2b2f36;
  --muted:#70757c;
  --line:#dde2e8;
  --band:#eef1f4;
  --thumb:#9aa8b8;
}
*{box-sizing:border-box;margin:0;padding:0}
html,body{width:804px;height:1200px;overflow:hidden}
body{font-family:"Open Sans",Arial,sans-serif;color:var(--ink);background:#fff;position:relative;font-size:10px}
.abs{position:absolute}

/* header */
.brand{left:24px;top:14px;display:flex;align-items:center;gap:8px}
.brand-mark{width:40px;height:40px;background:var(--navy)}
.brand-name{font-weight:700;color:var(--navy);font-size:12px;line-height:1.2;width:110px}
.phones{left:430px;top:14px;display:flex;gap:26px}
.phone-num{color:var(--blue);font-weight:700;font-size:12px}
.phone-label{color:var(--muted);font-size:8px}
.lang{right:24px;top:8px;font-size:8px;color:var(--muted)}
.social{right:24px;top:24px;display:flex;gap:4px}
.social span{width:18px;height:18px;background:var(--blue);display:block}
.nav{left:0;top:72px;width:804px;height:26px;display:flex;justify-content:center;gap:20px;align-items:center;font-size:10px;color:#4a4f57}
.nav .on{color:var(--blue);font-weight:600}

/* hero */
.hero{left:0;top:100px;width:804px;height:300px;background:linear-gradient(180deg,#c9d8e6 0%,#e6edf3 45%,#8f9eae 100%)}
.hero-title{left:28px;top:352px;color:#fff;font-size:22px;font-weight:600;text-shadow:0 1px 3px rgba(0,0,0,.35)}
.btn-pdf{left:640px;top:356px;width:138px;height:28px;background:var(--red);color:#fff;font-weight:700;font-size:9px;display:flex;align-items:center;justify-content:center;gap:6px}
.ticker{left:0;top:400px;width:804px;height:24px;background:var(--band);border-bottom:1px solid var(--line);display:flex;align-items:center;justify-content:center;font-size:8.5px;color:#4a4f57;gap:6px}
.ticker b{color:var(--blue);font-weight:600}
.ticker .arr{position:absolute;color:var(--muted);font-size:12px}

/* welcome */
.welcome{left:28px;top:440px;width:520px}
.welcome h1{font-size:17px;font-weight:600;color:var(--ink)}
.welcome h2{font-size:11px;font-weight:600;color:var(--blue);margin-top:3px}
.welcome p{font-size:9px;color:var(--muted);line-height:1.55;margin-top:10px}
.welcome p a{color:var(--blue);text-decoration:none;font-weight:600}
.cards{left:28px;top:566px;display:flex;gap:12px}
.card{width:165px;height:140px;position:relative;background:linear-gradient(160deg,#a7b6c6,#5e7189)}
.card-label{position:absolute;left:0;bottom:0;width:100%;height:26px;background:rgba(24,63,115,.75);color:#fff;font-size:11px;font-weight:600;display:flex;align-items:center;justify-content:center}

.press{left:572px;top:440px;width:208px;height:300px;border:1px solid var(--line)}
.press-head{background:var(--blue);color:#fff;font-weight:700;font-size:9px;padding:6px 10px;letter-spacing:.5px}
.press-item{display:flex;gap:8px;padding:9px 10px;border-bottom:1px solid var(--line)}
.press-item:last-child{border-bottom:none}
.thumb{width:48px;height:44px;flex:none;background:linear-gradient(160deg,#b7c3cf,#6f8196)}
.date{color:var(--blue);font-size:7.5px}
.snip{font-size:8px;color:var(--muted);line-height:1.4}

/* lower row */
.col{top:775px}
.col h3{font-size:9px;font-weight:700;letter-spacing:.4px;color:var(--ink);border-bottom:1px solid var(--line);padding-bottom:5px;margin-bottom:10px}
.blog{left:28px;width:240px}
.post{display:flex;gap:8px;margin-bottom:12px}
.post .thumb{width:50px;height:40px}
.videos{left:284px;width:262px}
.video{width:262px;height:160px;background:linear-gradient(160deg,#8595a7,#36465a);display:flex;align-items:center;justify-content:center}
.tests{left:562px;width:218px}
.quote{display:flex;gap:8px;margin-bottom:14px}
.avatar{width:42px;height:42px;border-radius:50%;flex:none;background:#b9c4cf}
.qname{color:var(--blue);font-size:8.5px;font-weight:600}

/* partners */
.partners{left:0;top:1000px;width:804px;text-align:center}
.partners h3{font-size:9px;font-weight:700;letter-spacing:.4px}
.badges{display:flex;justify-content:center;gap:34px;margin-top:12px}
.badges span{width:86px;height:22px;background:#d3d8de;border-radius:3px;display:block}

/* footer */
.footer{left:0;top:1072px;width:804px;height:104px;background:var(--footer);color:#fff}
.finfo{position:absolute;top:26px;display:flex;gap:8px}
.finfo b{font-size:9.5px;display:block;margin-bottom:2px}
.finfo div{font-size:8.5px;line-height:1.45}
.plume{position:absolute;right:24px;top:14px;width:196px;height:76px;background:#fff;display:flex;flex-direction:column;justify-content:center;padding:0 14px;border-radius:3px}
.plume-name{font-size:22px;font-weight:700;color:var(--navy)}
.plume-sub{font-size:7.5px;font-weight:700;color:var(--navy)}
.copy{left:0;top:1176px;width:804px;height:24px;background:var(--footer-dark);color:#d6e3f2;font-size:8px;display:flex;align-items:center;padding:0 24px;justify-content:space-between}
.copy .social{position:static;display:flex;gap:4px}
.copy .social span{width:12px;height:12px;background:#9cbbe0}
</style>
</head>
<body>

<header>
  <div class="abs brand"><span class="brand-mark"></span><span class="brand-name">SKYFORGE TECHNICS INC.</span></div>
  <div class="abs phones">
    <div><div class="phone-num">514-555-0142</div><div class="phone-label">Montreal AMO</div></div>
    <div><div class="phone-num">416-555-0163</div><div class="phone-label">Toronto AMO</div></div>
    <div><div class="phone-num">604-555-0127</div><div class="phone-label">Vancouver AMO</div></div>
  </div>
  <div class="abs lang">EN | FR | CN</div>
  <div class="abs social"><span></span><span></span><span></span></div>
  <nav class="abs nav">
    <span class="on">Home</span><span>Services</span><span>Locations</span><span>People</span><span>Quality</span><span>Sales Presentation</span><span>Press</span><span>Partners</span><span>Contact</span><span>Videos</span>
  </nav>
</header>

<section>
  <div class="abs hero" role="img" aria-label="Passenger jet in flight above the clouds, with inset photos of hangar repair work"></div>
  <div class="abs hero-title">Known by The Customers We Keep</div>
  <div class="abs btn-pdf">
    <svg width="10" height="10" viewBox="0 0 10 10"><path d="M5 1v6M2 4.5 5 7.5 8 4.5M1 9h8" stroke="#fff" stroke-width="1.4" fill="none"/></svg>
    DOWNLOAD PDF
  </div>
  <div class="abs ticker">
    <span class="arr" style="left:20px">‹</span>
    <b>May 6, 2014</b> – Skyforge Technics Inc. announces new Strategic Assistance Agreement with Northvale Systems [pdf]
    <span class="arr" style="right:20px">›</span>
  </div>
</section>

<section>
  <div class="abs welcome">
    <h1>Welcome to Skyforge Technics Inc.</h1>
    <h2>Founded in 1962 in Montreal, Canada as Skyforge AeroMarine</h2>
    <p>Evolved from a distributor and machine shop to a full service maintenance, repair and overhaul (MRO) company in the 1990s. Expanded into a comprehensive network of 30 repair stations and 8 line maintenance support locations at major airports in North America and the UK. <a>[ReadMore]</a></p>
  </div>
  <div class="abs cards">
    <div class="card" role="img" aria-label="Technicians team in the hangar"><div class="card-label">Our People</div></div>
    <div class="card" role="img" aria-label="Aircraft component repair bench"><div class="card-label">Our Services</div></div>
    <div class="card" role="img" aria-label="Quality inspection of aircraft parts"><div class="card-label">Our Quality</div></div>
  </div>

  <aside class="abs press">
    <div class="press-head">PRESS ROOM</div>
    <div class="press-item"><div class="thumb" role="img" aria-label="Press photo"></div><div><div class="date">17 Jan 2014</div><div class="snip">The standard Lorem Ipsum used since the connectior adipiscing elit connectetur.</div></div></div>
    <div class="press-item"><div class="thumb" role="img" aria-label="Press photo"></div><div><div class="date">17 Jan 2014</div><div class="snip">The standard Lorem Ipsum used since the connectior adipiscing elit connectetur.</div></div></div>
    <div class="press-item"><div class="thumb" role="img" aria-label="Press photo"></div><div><div class="date">17 Jan 2014</div><div class="snip">The standard Lorem Ipsum used since the connectior adipiscing elit connectetur.</div></div></div>
    <div class="press-item"><div class="thumb" role="img" aria-label="Press photo"></div><div><div class="date">17 Jan 2014</div><div class="snip">The standard Lorem Ipsum used since the connectior adipiscing elit connectetur.</div></div></div>
  </aside>
</section>

<section>
  <div class="abs col blog">
    <h3>OUR BLOG POSTS</h3>
    <div class="post"><div class="thumb" role="img" aria-label="Blog photo"></div><div><div class="date">17 Jan 2014 | 12 Comments</div><div class="snip">The standard Lorem Ipsum used since the connectior adipiscing elit connectetur.</div></div></div>
    <div class="post"><div class="thumb" role="img" aria-label="Blog photo"></div><div><div class="date">17 Jan 2014 | 12 Comments</div><div class="snip">The standard Lorem Ipsum used since the connectior adipiscing elit connectetur.</div></div></div>
    <div class="post"><div class="thumb" role="img" aria-label="Blog photo"></div><div><div class="date">17 Jan 2014 | 12 Comments</div><div class="snip">The standard Lorem Ipsum used since the connectior adipiscing elit connectetur.</div></div></div>
  </div>
  <div class="abs col videos">
    <h3>OUR VIDEOS</h3>
    <div class="video" role="img" aria-label="Video still of aircraft maintenance work">
      <svg width="46" height="46" viewBox="0 0 46 46"><circle cx="23" cy="23" r="22" fill="#d7332b"/><path d="M18 14 32 23 18 32Z" fill="#fff"/></svg>
    </div>
  </div>
  <div class="abs col tests">
    <h3>TESTIMONIALS</h3>
    <div class="quote"><div class="avatar" role="img" aria-label="Customer portrait"></div><div><div class="qname">Andre L.</div><div class="snip">The standard Lorem Ipsum used since the connectior adipiscing elit connectetur.</div></div></div>
    <div class="quote"><div class="avatar" role="img" aria-label="Customer portrait"></div><div><div class="qname">Marie C.</div><div class="snip">The standard Lorem Ipsum used since the connectior adipiscing elit connectetur.</div></div></div>
  </div>
</section>

<section class="abs partners">
  <h3>PARTNERS</h3>
  <div class="badges"><span></span><span></span><span></span><span></span><span></span><span></span></div>
</section>

<footer>
  <div class="abs footer">
    <div class="finfo" style="left:28px">
      <svg width="18" height="18" viewBox="0 0 18 18"><path d="M3 17V3h8v14M11 7h4v10M5 6h2M5 9h2M5 12h2" stroke="#fff" stroke-width="1.4" fill="none"/></svg>
      <div><b>Corporate Office</b>45 Harbourline Road<br>Dorval, Quebec, H9P 2X6</div>
    </div>
    <div class="finfo" style="left:218px">
      <svg width="18" height="18" viewBox="0 0 18 18"><path d="M4 2h3l1.5 4-2 1.3a9 9 0 0 0 4.2 4.2l1.3-2 4 1.5v3c0 1-1 2-2 2A13 13 0 0 1 2 4c0-1 1-2 2-2Z" fill="#fff"/></svg>
      <div><b>Phone</b>(514) 555-0188</div>
    </div>
    <div class="finfo" style="left:368px">
      <svg width="18" height="18" viewBox="0 0 18 18"><rect x="2" y="4" width="14" height="10" fill="none" stroke="#fff" stroke-width="1.4"/><path d="M2 4l7 6 7-6" fill="none" stroke="#fff" stroke-width="1.4"/></svg>
      <div><b>Email Information</b>info@skyforgenorth.example</div>
    </div>
    <div class="plume">
      <div class="plume-name">PLUME</div>
      <div class="plume-sub">Skyforge Validation Bureau Partners inc.</div>
    </div>
  </div>
  <div class="abs copy">
    <span>Copyright ©2014 Skyforge Technics Inc. All Rights Reserved</span>
    <span class="social"><span></span><span></span><span></span></span>
  </div>
</footer>

</body>
</html>
```